Website design using a wordpress template I purchased

I have purchased a wordpress template called "Vantrel" from Plumora and would like to design a website using it for a financial services company. The site simply needs to be informational about the company and a blog. Nothing too involved. The company provides paymaster / escrow services for commodity transactions. I am working on the logo currently and will have it ready to provide shortly. I can provide the content for the informational portion of the site as well. I would like some quick tutoring regarding how to administer the blog portion of the site once built.

```html
<!DOCTYPE html>
<html lang="en">
<head>
<meta charset="utf-8">
<title>Financial Services Company — Paymaster / Escrow Services</title>
<link href="https://fonts.googleapis.com/css2?family=Montserrat:wght@400;500;600;700&display=swap" rel="stylesheet">
<style>
:root{
  --orange:#e8801f;
  --orange-tint:#fbe6d2;
  --ink:#2b2d33;
  --muted:#6f727b;
  --soft-bg:#f5f6fb;
  --ghost:#eceef7;
  --footer:#1e2024;
  --white:#ffffff;
}
*{box-sizing:border-box;margin:0;padding:0}
html,body{width:1200px;height:4298px;overflow:hidden}
body{font-family:'Montserrat',sans-serif;color:var(--ink);background:var(--white);position:relative}
.abs{position:absolute}
a{color:inherit;text-decoration:none}

/* hero */
.hero{left:0;top:0;width:1200px;height:667px;background:linear-gradient(120deg,#3a3f48 0%,#8e97a3 35%,#d9dde2 55%,#6b5545 80%,#2a2c31 100%)}
.hero-shade{left:0;top:0;width:1200px;height:667px;background:linear-gradient(90deg,rgba(20,24,32,.55) 0%,rgba(20,24,32,.15) 60%,rgba(20,24,32,.35) 100%)}
.brand{left:110px;top:40px;font-size:27px;font-weight:700;line-height:34px;color:var(--white)}
.topbar{left:646px;top:26px;font-size:17px;color:var(--white);display:flex;gap:10px;align-items:center;white-space:nowrap}
.topbar svg{vertical-align:-2px;margin-right:4px}
.nav{left:701px;top:74px;display:flex;gap:24px;font-size:17px;font-weight:600;color:var(--white)}
.nav .active{color:var(--orange)}
.hero-title{left:110px;top:205px;font-size:46px;font-weight:700;line-height:58px;color:var(--white)}
.btn-orange{left:110px;top:411px;width:209px;height:65px;border-radius:33px;background:var(--orange);color:var(--white);font-size:18px;font-weight:600;display:flex;align-items:center;justify-content:center}

/* welcome */
.welcome-title{left:0;top:735px;width:1200px;text-align:center;font-size:40px;font-weight:600;line-height:49px}
.welcome-text{left:220px;top:855px;width:760px;text-align:center;font-size:16px;line-height:27.5px;color:var(--muted)}
.read-more{font-weight:600;color:var(--orange);font-size:17px}
.welcome-more{left:0;top:992px;width:1200px;text-align:center}
.video{left:309px;top:1060px;width:584px;height:320px;background:linear-gradient(135deg,#6a5240,#b8a58e 45%,#8d8a87 70%,#4b4f57)}
.play{left:559px;top:1182px;width:66px;height:66px;border-radius:50%;background:#1f2024;display:flex;align-items:center;justify-content:center}

/* ghost words */
.ghost{font-size:78px;font-weight:700;color:var(--ghost);line-height:1;white-space:nowrap}

/* about */
.about{left:0;top:1507px;width:1200px;height:718px;background:var(--soft-bg);overflow:hidden}
.step{width:228px;background:var(--white);box-shadow:0 4px 18px rgba(40,50,90,.06);text-align:center;font-size:17px;font-weight:600;line-height:25px;padding:0 14px;z-index:1}
.step-icon{width:100px;height:100px;margin:30px auto 20px;border-radius:50%;background:var(--orange-tint)}
.step-num{font-size:46px;font-weight:700;color:#b9bcc6;line-height:1;z-index:2}
.about-title{left:649px;top:1622px;font-size:40px;font-weight:600;line-height:48px}
.about-text{left:649px;top:1798px;width:478px;font-size:16px;line-height:27.5px;color:var(--muted)}

/* expect */
.expect-title{left:110px;top:2285px;font-size:40px;font-weight:600;line-height:48px}
.checks{left:110px;top:2462px;width:410px;list-style:none;font-size:16px;line-height:24px;color:#4a4d55}
.checks li{position:relative;padding-left:24px;margin-bottom:24px}
.checks li svg{position:absolute;left:0;top:4px}
.expect-photo{left:606px;top:2225px;width:594px;height:687px;background:linear-gradient(160deg,#27304a 0%,#3a4a6a 40%,#6f7682 70%,#bfc3c9 100%)}
.why{left:716px;top:2840px;font-size:74px;line-height:1;font-weight:700;color:rgba(255,255,255,.28);white-space:nowrap}

/* blog */
.blog-title{left:0;top:2972px;width:1200px;text-align:center;font-size:37px;font-weight:600}
.card{top:3058px;width:310px;height:459px;background:var(--white);box-shadow:0 4px 20px rgba(40,50,90,.1);border-radius:4px;overflow:hidden}
.card-img{height:210px}
.card-body{padding:22px 24px}
.card h3{font-size:19px;font-weight:600;line-height:26px}
.card .date{margin-top:8px;font-size:16px;color:var(--muted)}
.card .date svg{vertical-align:-2px;margin-right:4px}
.card p{margin-top:14px;font-size:16px;line-height:23px;color:var(--muted)}
.card .read-more{display:block;margin-top:14px}
.arrow{top:3261px;width:50px;height:50px;border-radius:50%;border:1.5px solid #c9ccd4;background:var(--white);display:flex;align-items:center;justify-content:center}

/* cta */
.cta{left:0;top:3627px;width:1200px;height:299px;background:var(--orange);color:var(--white);text-align:center}
.cta h2{margin-top:58px;font-size:38px;font-weight:600}
.cta p{margin-top:10px;font-size:22px}
.btn-white{display:inline-flex;margin-top:28px;width:194px;height:67px;border-radius:34px;background:var(--white);color:var(--ink);font-size:18px;font-weight:600;align-items:center;justify-content:center}

/* footer */
.footer{left:0;top:3926px;width:1200px;height:372px;background:var(--footer);color:var(--white)}
.footer-brand{left:110px;top:78px;font-size:34px;font-weight:700;line-height:44px}
.footer h4{font-size:20px;font-weight:600}
.links{left:521px;top:68px}
.links ul{list-style:none;margin-top:14px;font-size:16px;line-height:33.5px}
.contact{left:743px;top:68px;font-size:16px;line-height:24px}
.contact div{position:relative;padding-left:20px}
.contact svg{position:absolute;left:0;top:4px}
.rule{left:110px;top:288px;width:980px;height:1px;background:#3a3d44}
.copy{left:110px;top:312px;font-size:16px}
.social{top:306px;width:36px;height:36px;border-radius:50%;border:1.5px solid var(--orange)}
</style>
</head>
<body>

<!-- Hero -->
<div class="abs hero" role="img" aria-label="Colleagues reviewing financial charts on a tablet at a desk"></div>
<div class="abs hero-shade"></div>
<div class="abs brand">Financial services<br>company</div>
<div class="abs topbar">
  <span><svg width="14" height="14" viewBox="0 0 24 24"><path fill="#e8801f" d="M6.6 10.8a15.1 15.1 0 006.6 6.6l2.2-2.2c.3-.3.7-.4 1-.2 1.1.4 2.3.6 3.6.6.6 0 1 .4 1 1V20c0 .6-.4 1-1 1A17 17 0 013 4c0-.6.4-1 1-1h3.5c.6 0 1 .4 1 1 0 1.3.2 2.5.6 3.6.1.3 0 .7-.2 1z"/></svg>1 888 555 0142</span>
  <span>|</span>
  <span><svg width="15" height="12" viewBox="0 0 24 18"><rect width="24" height="18" rx="2" fill="#e8801f"/><path d="M1 2l11 8 11-8" stroke="#fff" stroke-width="2" fill="none"/></svg>info@ledgerwellfinance.com</span>
</div>
<nav class="abs nav">
  <a class="active" href="#">Home</a><a href="#">About</a><a href="#">Services</a><a href="#">Blog</a><a href="#">Contact</a>
</nav>
<h1 class="abs hero-title">Paymaster / Escrow<br>services For Commodity<br>Transactions</h1>
<a class="abs btn-orange" href="#">GET MORE INFO</a>

<!-- Welcome -->
<h2 class="abs welcome-title">Welcome to<br>Financial Services Company</h2>
<p class="abs welcome-text">Lorem ipsum dolor sit amet, consectetur adipiscing elit, sed do eiusmod tempor incidi dunt ut labore et dolore magna aliqua. Ut enim ad minim veniam, quis nostrud exercitation ullamco laboris nisi ut aliquip ex ea commodo consequa uis aute irure dolor in repreh enderit in voluptate velit esse cillum dolore eu fugiat nullap.</p>
<div class="abs welcome-more"><a class="read-more" href="#">READ MORE</a></div>
<div class="abs video" role="img" aria-label="Video still of a team working with laptops and printed charts"></div>
<div class="abs play"><svg width="22" height="24" viewBox="0 0 22 24"><path d="M3 2l17 10L3 22z" fill="#fff"/></svg></div>

<!-- About -->
<div class="abs about">
  <div class="abs ghost" style="left:760px;top:632px">SERVICES</div>
</div>
<div class="abs ghost" style="left:0;top:1444px">ABOUT US</div>

<div class="abs step-num" style="left:100px;top:1558px">1</div>
<div class="abs step" style="left:112px;top:1572px;height:244px">
  <div class="step-icon" role="img" aria-label="Icon: receiving funds from the buyer"></div>
  Receive funds from the buyer
</div>
<div class="abs step-num" style="left:358px;top:1610px">2</div>
<div class="abs step" style="left:367px;top:1632px;height:244px">
  <div class="step-icon" role="img" aria-label="Icon: funds held in escrow"></div>
  Maintain funds in escrow
</div>
<div class="abs step-num" style="left:100px;top:1830px">3</div>
<div class="abs step" style="left:112px;top:1848px;height:242px">
  <div class="step-icon" role="img" aria-label="Icon: funds paid out to the seller"></div>
  Disburse funds to the seller
</div>
<div class="abs step-num" style="left:364px;top:1888px">4</div>
<div class="abs step" style="left:367px;top:1908px;height:243px">
  <div class="step-icon" role="img" aria-label="Icon: tax paperwork"></div>
  Handle IRS forms &amp; tax-related paperwork
</div>

<h2 class="abs about-title">Paymaster / Escrow<br>services for commodity<br>transactions</h2>
<p class="abs about-text">Nemo enim ipsam voluptatem quia voluptas siaspern atur aut odit aut fugit, sed quia consequuntur magni dolores eos qui ratione voluptatem sequi nesciunt. Ne que porro quisquam est, qui dolorem ipsum quia dolor sit amet, con sectetur, adipisci velit, sed quianumquam eius modi tempora incidunt ut.</p>

<!-- What to expect -->
<h2 class="abs expect-title">What to Expect When<br>Using Paymaster/<br>Escrow Services</h2>
<ul class="abs checks">
  <li><svg width="15" height="15" viewBox="0 0 16 16"><circle cx="8" cy="8" r="8" fill="#e8801f"/><path d="M4.5 8.2l2.3 2.3 4.7-4.7" stroke="#fff" stroke-width="1.8" fill="none"/></svg>A copy of valid ID from each party, such as a passport or driver’s license</li>
  <li><svg width="15" height="15" viewBox="0 0 16 16"><circle cx="8" cy="8" r="8" fill="#e8801f"/><path d="M4.5 8.2l2.3 2.3 4.7-4.7" stroke="#fff" stroke-width="1.8" fill="none"/></svg>W-9 forms for each US citizen involved in the transaction</li>
  <li><svg width="15" height="15" viewBox="0 0 16 16"><circle cx="8" cy="8" r="8" fill="#e8801f"/><path d="M4.5 8.2l2.3 2.3 4.7-4.7" stroke="#fff" stroke-width="1.8" fill="none"/></svg>W-8BEN forms for non-US citizens involved</li>
  <li><svg width="15" height="15" viewBox="0 0 16 16"><circle cx="8" cy="8" r="8" fill="#e8801f"/><path d="M4.5 8.2l2.3 2.3 4.7-4.7" stroke="#fff" stroke-width="1.8" fill="none"/></svg>A copy of the payment agreement</li>
  <li><svg width="15" height="15" viewBox="0 0 16 16"><circle cx="8" cy="8" r="8" fill="#e8801f"/><path d="M4.5 8.2l2.3 2.3 4.7-4.7" stroke="#fff" stroke-width="1.8" fill="none"/></svg>Copies of all other relevant transactional documents</li>
  <li><svg width="15" height="15" viewBox="0 0 16 16"><circle cx="8" cy="8" r="8" fill="#e8801f"/><path d="M4.5 8.2l2.3 2.3 4.7-4.7" stroke="#fff" stroke-width="1.8" fill="none"/></svg>Report of pending dealings with which we’re involved</li>
</ul>
<div class="abs expect-photo" role="img" aria-label="Businessman in a suit signing a document with a pen"></div>
<div class="abs why">WHY US</div>

<!-- Blog -->
<h2 class="abs blog-title">Latest Blog</h2>
<div class="abs arrow" style="left:32px"><svg width="12" height="20" viewBox="0 0 12 20"><path d="M10 2L2 10l8 8" stroke="#555" stroke-width="2" fill="none"/></svg></div>
<div class="abs arrow" style="left:1117px"><svg width="12" height="20" viewBox="0 0 12 20"><path d="M2 2l8 8-8 8" stroke="#555" stroke-width="2" fill="none"/></svg></div>

<article class="abs card" style="left:112px">
  <div class="card-img" role="img" aria-label="Pen on a financial statement beside stacks of coins" style="background:linear-gradient(120deg,#b8874a,#e9e2d6 55%,#c9c3b8)"></div>
  <div class="card-body">
    <h3>Nemo enim ipsam volseup atem quia volupt..</h3>
    <div class="date"><svg width="13" height="13" viewBox="0 0 14 14"><rect x="1" y="2" width="12" height="11" rx="1" fill="#e8801f"/><rect x="3" y="6" width="8" height="5" fill="#fff"/></svg>20/10/2022</div>
    <p>Ut enim ad minima veniam quis nostrum exercitationem ullam corporis suscipit labo.</p>
    <a class="read-more" href="#">READ MORE</a>
  </div>
</article>
<article class="abs card" style="left:446px">
  <div class="card-img" role="img" aria-label="Two people discussing paperwork at a desk with a laptop" style="background:linear-gradient(120deg,#5e6670,#d8d4cc 50%,#8a7e70)"></div>
  <div class="card-body">
    <h3>Nemo enim ipsam volseup atem quia volupt..</h3>
    <div class="date"><svg width="13" height="13" viewBox="0 0 14 14"><rect x="1" y="2" width="12" height="11" rx="1" fill="#e8801f"/><rect x="3" y="6" width="8" height="5" fill="#fff"/></svg>20/10/2022</div>
    <p>Ut enim ad minima veniam quis nostrum exercitationem ullam corporis suscipit labo.</p>
    <a class="read-more" href="#">READ MORE</a>
  </div>
</article>
<article class="abs card" style="left:778px">
  <div class="card-img" role="img" aria-label="Tax forms on a desk with a pen and stationery" style="background:linear-gradient(120deg,#7aa8d0,#eef0f2 45%,#d7dadf)"></div>
  <div class="card-body">
    <h3>Nemo enim ipsam volseup atem quia volupt..</h3>
    <div class="date"><svg width="13" height="13" viewBox="0 0 14 14"><rect x="1" y="2" width="12" height="11" rx="1" fill="#e8801f"/><rect x="3" y="6" width="8" height="5" fill="#fff"/></svg>20/10/2022</div>
    <p>Ut enim ad minima veniam quis nostrum exercitationem ullam corporis suscipit labo.</p>
    <a class="read-more" href="#">READ MORE</a>
  </div>
</article>

<div class="abs ghost" style="left:0;top:3565px">POST</div>

<!-- CTA -->
<section class="abs cta">
  <h2>How can we help?</h2>
  <p>Get in touch with our Paymaster/Escrow experts</p>
  <a class="btn-white" href="#">CONTACT US</a>
</section>

<!-- Footer -->
<footer class="abs footer">
  <div class="abs footer-brand">Financial Services<br>Company</div>
  <div class="abs links">
    <h4>Quick Links</h4>
    <ul><li>Home</li><li>About</li><li>Services</li><li>Blog</li><li>Contact</li></ul>
  </div>
  <div class="abs contact">
    <h4>Contact Us</h4>
    <div style="margin-top:16px"><svg width="11" height="15" viewBox="0 0 12 16"><path d="M6 0a6 6 0 016 6c0 4.5-6 10-6 10S0 10.5 0 6a6 6 0 016-6z" fill="#e8801f"/><circle cx="6" cy="6" r="2.2" fill="#1e2024"/></svg>48 Harlow Lane<br>Brightmoor OH 44102</div>
    <div style="margin-top:22px"><svg width="13" height="13" viewBox="0 0 24 24"><path fill="#e8801f" d="M6.6 10.8a15.1 15.1 0 006.6 6.6l2.2-2.2c.3-.3.7-.4 1-.2 1.1.4 2.3.6 3.6.6.6 0 1 .4 1 1V20c0 .6-.4 1-1 1A17 17 0 013 4c0-.6.4-1 1-1h3.5c.6 0 1 .4 1 1 0 1.3.2 2.5.6 3.6.1.3 0 .7-.2 1z"/></svg>1 888 555 0142</div>
    <div style="margin-top:24px"><svg width="15" height="12" viewBox="0 0 24 18"><rect width="24" height="18" rx="2" fill="#e8801f"/><path d="M1 2l11 8 11-8" stroke="#1e2024" stroke-width="2" fill="none"/></svg>info@ledgerwellfinance.com</div>
  </div>
  <div class="abs rule"></div>
  <div class="abs copy">© 2022, Financial Services Company. All rights reserved.</div>
  <div class="abs social" style="left:962px" aria-label="Social link"></div>
  <div class="abs social" style="left:1007px" aria-label="Social link"></div>
  <div class="abs social" style="left:1052px" aria-label="Social link"></div>
</footer>

</body>
</html>
```